Import Export Business Needs a Website

We need a website design that is fluid and utilizing todays visual appeal. HTML5 Wordpress that can be fully customized after a turnkey solution by us. We need to be able to have full control of the site's backend and allow for creative content to be easily changed.

We own a template that we would like to have utilized and we already have a LOGO, we would like site content and language to be provided for us. Basic informational site, no need for shopping carts, blogs, or surveys.

We want to be as similar as possible as the appearance to https://www.brenvaletiles.com

These below are in our industry (We want a better website than our Competitors)
Competition:

http://www.pulmorglobal.com/index.html
http://www.vxmerchants.com/
http://www.orvel-bimako-hemp.com/
http://www.ltquorrel.com/index.html
http://www.fenvista.com/index.php

Customers:
https://www.brenvaletiles.com/
http://www.deltismats.com/en
http://www.zqmats.com/

Supplier:
http://tovelhold.com/
http://www.varnopex.com/
http://www.lumbrewoven.com/en/index.html

Project Deadline Extended
Reason: We have been extremely busy with tracking a shipment we have not had time to review the designs in depth or get with a designer to customize settings. We will be selecting someone tomorrow to work with and would like to have the weekend and the first few days of next week to discuss the site in detail.

Target Market(s)

Textile Carpet Fibers Fabric

Industry/Entity Type

Business

Number of Pages Required

5+ page

Font styles to use
Serif
Sans Serif
Other font styles liked:
• font has been uploaded for use in logo and small accents

Colors
3176b5
ffffff
85cae6
3377b5
0255a3
34a6d7
c4c4c4
c3c3c3
aaaaaa

Requirements
Must have
• Project must utilize provided template or substitute template can be provided but must be for wordpress. Fonts have been uploaded for LOGO provided.
Nice to have
• Nice to have metrics to know site visitors and demographics
Should not have
• ecommerce, shopping carts

```html
<!DOCTYPE html>
<html lang="en">
<head>
<meta charset="utf-8">
<title>Corvane International</title>
<link href="https://fonts.googleapis.com/css2?family=Questrial&family=Poppins:wght@300;400;500&display=swap" rel="stylesheet">
<style>
:root{
  --navy:#1b2f57;
  --navy-deep:#142646;
  --lavender:#dfe1ee;
  --field:#dcdff0;
  --grey-bg:#ececec;
  --footer-bg:#e6e6e6;
  --ink:#2b2b2b;
  --muted:#6b6b6b;
  --white:#ffffff;
  --line:#bdbdbd;
}
*{box-sizing:border-box;margin:0;padding:0}
html,body{width:1200px;height:4401px;overflow:hidden;background:var(--white)}
body{position:relative;font-family:"Poppins",sans-serif;color:var(--ink)}
.abs{position:absolute}
.hero{left:0;top:0;width:1200px;height:651px;background:linear-gradient(110deg,#8b9098 0%,#a3a7ae 35%,#6f7c93 65%,#2e3e5c 100%)}
.menu-icon{left:590px;top:70px;width:20px;height:16px}
.brand{left:0;top:230px;width:1200px;text-align:center;color:var(--white);font-family:"Questrial",sans-serif}
.brand-dot{width:70px;height:70px;border-radius:50%;background:#3a6fb0;margin:0 auto 14px}
.brand-name{font-size:44px;letter-spacing:4px;line-height:1.1}
.brand-sub{font-size:22px;letter-spacing:5px}
.philosophy{left:555px;top:549px;width:498px;height:639px;background:var(--navy);color:var(--white);padding:70px 60px}
.philosophy::after{content:"";position:absolute;left:22px;top:22px;right:22px;bottom:22px;border:1px solid rgba(255,255,255,.35)}
h2.box-title{font-family:"Questrial",sans-serif;font-weight:400;font-size:30px;margin-bottom:26px}
.philosophy p{font-size:11.5px;line-height:2.2}
.btn-outline{display:inline-block;border:1px solid currentColor;font-size:12px;padding:10px 30px;margin-top:30px;position:relative;z-index:1}
.burlap{left:229px;top:728px;width:364px;height:314px;background:linear-gradient(135deg,#a89274,#6e5a42 60%,#4f3f2d)}
.experience{left:147px;top:1036px;width:525px;height:240px;background:var(--lavender);padding:50px 45px}
.experience h2{font-size:27px;margin-bottom:14px;color:#222}
.experience p{font-size:11px;line-height:2;color:var(--muted)}
.link-under{display:inline-block;font-size:11px;margin-top:14px;padding-bottom:4px;border-bottom:1px solid #444;position:relative}
.link-under::before{content:"";position:absolute;left:0;right:0;top:-6px;border-top:1px solid #999}
.works-bg{left:0;top:1276px;width:1200px;height:1822px;background:var(--grey-bg)}
.section-head{left:0;width:1200px;text-align:center;font-family:"Questrial",sans-serif;color:#333}
.section-head .small{font-size:21px;letter-spacing:2px}
.section-head .big{font-size:38px;letter-spacing:3px;line-height:1}
.card{background:var(--white)}
.card-photo{position:absolute}
.card-text{position:absolute;text-align:center;padding:0 40px}
.card-text h3{font-family:"Questrial",sans-serif;font-weight:400;font-size:36px;letter-spacing:2px;margin-bottom:28px}
.card-text p{font-size:11px;line-height:2;color:var(--muted)}
.card-text .link-under{margin-top:26px;padding:6px 30px}
.btn-solid{background:var(--navy);color:var(--white);font-size:17px;display:flex;align-items:center;justify-content:center;letter-spacing:1px}
.why{left:0;top:3098px;width:1200px;height:423px;background:var(--navy);color:var(--white);text-align:center}
.why h2{font-family:"Questrial",sans-serif;font-weight:400;font-size:36px;position:absolute;top:38px;width:100%}
.feature{position:absolute;top:140px;width:340px;font-size:15px;line-height:1.9}
.feature svg{display:block;margin:0 auto 20px}
.why .btn-outline{position:absolute;left:513px;top:352px;width:186px;margin:0;text-align:center;padding:8px 0;font-size:13px}
.field{position:absolute;font-size:12px;color:var(--muted);border-bottom:1px solid #ccc;padding-bottom:8px}
.message-box{left:197px;top:3920px;width:830px;height:123px;background:var(--field)}
.footer{left:0;top:4216px;width:1200px;height:185px;background:var(--footer-bg)}
.footer nav{position:absolute;top:38px;width:100%;display:flex;justify-content:center;gap:60px;font-family:"Questrial",sans-serif;font-size:20px;color:#222}
.socials{position:absolute;top:96px;width:100%;display:flex;justify-content:center;gap:12px}
.socials span{width:28px;height:28px;border:2px solid #222;border-radius:50%}
.copy{position:absolute;top:152px;width:100%;text-align:center;font-size:11px;color:#444}
</style>
</head>
<body>

<header class="abs hero" role="img" aria-label="Businessman holding a tablet in front of a city skyline"></header>
<svg class="abs menu-icon" viewBox="0 0 20 16"><rect width="20" height="2" fill="#fff"/><rect y="7" width="20" height="2" fill="#fff"/><rect y="14" width="20" height="2" fill="#fff"/></svg>
<div class="abs brand">
  <div class="brand-dot"></div>
  <div class="brand-name">CORVANE</div>
  <div class="brand-sub">INTERNATIONAL</div>
</div>

<div class="abs burlap" role="img" aria-label="Rolled burlap fabric with twine"></div>

<section class="abs philosophy">
  <h2 class="box-title">Philosophy</h2>
  <p>Lorem Ipsum is simply dummy text of the printing and typesetting industry. Lorem Ipsum has been the industry's standard dummy text ever since the 1500s, when an unknown printer took a galley of type and scrambled it to make a type specimen book. It has survived not only five centuries, but also the leap into electronic typesetting, remaining essentially unchanged. It was popularised in the 1960s with the release of Letraset sheets containing Lorem Ipsum passages, and more recently with desktop publishing software like Aldus PageMaker including versions of Lorem Ipsum.</p>
  <span class="btn-outline">LEARN MORE</span>
</section>

<section class="abs experience">
  <h2 class="box-title">Experience</h2>
  <p>Lorem Ipsum is simply dummy text of the printing and typesetting industry. Lorem Ipsum has been the industry's standard dummy text ever since the 1500s, when an unknown printer took a galley of type and scrambled it to make a type specimen book. It has survived not only five centuries, but also the leap into electronic typesetting, remaining essentially unchanged.</p>
  <span class="link-under">VIEW PORTFOLIO</span>
</section>

<div class="abs works-bg"></div>
<div class="abs section-head" style="top:1432px"><div class="small">RECENT</div><div class="big">WORKS</div></div>

<article class="abs card" style="left:126px;top:1555px;width:948px;height:440px">
  <div class="card-photo" role="img" aria-label="Hanging burlap biscuit sacks with tags" style="left:0;top:0;width:473px;height:440px;background:linear-gradient(160deg,#5a4630,#b79f7c 45%,#8c7353)"></div>
  <div class="card-text" style="left:473px;top:78px;width:475px">
    <h3>Lenoleum</h3>
    <p>Lorem Ipsum is simply dummy text of the printing and typesetting industry. Lorem Ipsum has been the industry's standard dummy text ever since the 1500s, when an unknown printer took a galley of type and scrambled it to make a type specimen book. It has survived not only five centuries, but also the leap into electronic typesetting, remaining essentially unchanged. It was popularised in the 1960s with the release of Letraset sheets containing Lorem Ipsum passages.</p>
    <span class="link-under">VIEW MORE</span>
  </div>
</article>

<article class="abs card" style="left:126px;top:2036px;width:948px;height:467px">
  <div class="card-text" style="left:0;top:80px;width:338px;padding:0 20px">
    <h3>YARN</h3>
    <p>Lorem Ipsum is simply dummy text of the printing and typesetting industry. Lorem Ipsum has been the industry's standard dummy text ever since the 1500s, when an unknown printer took a galley of type and scrambled it to make a type specimen book. It has survived not only five centuries, but also the leap into electronic typesetting, remaining essentially unchanged.</p>
    <span class="link-under">VIEW MORE</span>
  </div>
</article>
<div class="abs" role="img" aria-label="Burlap sacks filled with nuts on a wicker surface" style="left:464px;top:2036px;width:663px;height:446px;background:linear-gradient(135deg,#7a5a3a,#c8a677 45%,#9b7a52 75%,#5b4128)"></div>

<article class="abs card" style="left:126px;top:2526px;width:948px;height:437px">
  <div class="card-photo" role="img" aria-label="Close-up of folded burlap cloth" style="left:0;top:0;width:473px;height:437px;background:radial-gradient(circle at 60% 40%,#9b6f45,#5c3c22 70%,#3c2615)"></div>
  <div class="card-text" style="left:473px;top:78px;width:475px">
    <h3>GEOTEXTILE</h3>
    <p>Lorem Ipsum is simply dummy text of the printing and typesetting industry. Lorem Ipsum has been the industry's standard dummy text ever since the 1500s, when an unknown printer took a galley of type and scrambled it to make a type specimen book. It has survived not only five centuries, but also the leap into electronic typesetting, remaining essentially unchanged. It was popularised in the 1960s with the release of Letraset sheets containing Lorem Ipsum passages.</p>
    <span class="link-under">VIEW MORE</span>
  </div>
</article>

<div class="abs btn-solid" style="left:458px;top:3004px;width:284px;height:53px">SEE PORTFOLIO</div>

<section class="abs why">
  <h2>Why We Are</h2>
  <div class="feature" style="left:65px">
    <svg width="56" height="62" viewBox="0 0 56 62"><path d="M28 3 L52 12 V30 C52 45 41 55 28 59 C15 55 4 45 4 30 V12 Z" fill="none" stroke="#fff" stroke-width="4"/><path d="M17 31 L25 39 L40 23" fill="none" stroke="#fff" stroke-width="5"/></svg>
    BUILT ON TRUST, RELIABILITY &amp;<br>YEARS OF EXPERIENCE
  </div>
  <div class="feature" style="left:430px">
    <svg width="50" height="62" viewBox="0 0 50 62"><path d="M3 3 H47 V59 L25 48 L3 59 Z" fill="#fff"/><path d="M25 14 L29 24 L40 24 L31 31 L34 42 L25 35 L16 42 L19 31 L10 24 L21 24 Z" fill="#1b2f57"/></svg>
    A TEAM WITH A TIME - HONORED<br>COMMITMENT TO QUALITY GOODS &amp;<br>SERVICE
  </div>
  <div class="feature" style="left:800px">
    <svg width="74" height="62" viewBox="0 0 74 62" fill="none" stroke="#fff" stroke-width="3"><rect x="22" y="4" width="30" height="26"/><rect x="4" y="32" width="32" height="26"/><rect x="38" y="32" width="32" height="26"/><path d="M37 4 V14 M20 32 V42 M54 32 V42"/></svg>
    LARGEST EXPORT &amp;<br>IMPORT COMPANY
  </div>
  <span class="btn-outline">LEARN MORE</span>
</section>

<div class="abs section-head" style="top:3627px"><div class="small">CONTACT</div><div class="big" style="font-size:34px">REACH US</div></div>
<div class="field" style="left:197px;top:3754px;width:405px">Email Address</div>
<div class="field" style="left:622px;top:3754px;width:405px">Phone Number</div>
<div class="field" style="left:197px;top:3825px;width:830px">Subject</div>
<div class="field" style="left:197px;top:3888px;width:830px;border:0">Message</div>
<div class="abs message-box"></div>
<div class="abs btn-solid" style="left:487px;top:4107px;width:249px;height:59px">Send Message</div>

<footer class="abs footer">
  <nav><span>Home</span><span>About</span><span>Works</span><span>Services</span><span>Contact</span></nav>
  <div class="socials"><span></span><span></span><span></span><span></span></div>
  <div class="copy">© 2017 Corvane International All Rights Reserved</div>
</footer>

</body>
</html>
```